Business Card Design for Marketing Firm

Looking for business card design for higher end marketing firm. Clean but impressionable/trendy. We are a marketing firm that represents manufacturers in the foodservice equipment and supply industry. Our customers are end users such has hotels, restaurants, country clubs, convention centers and casinos as well as distributors of restaurants supplies and equipment, and manufacturers of foodservice equipment and supplies.
Target Market(s)
Hotels, Restaurants, Supply & Equipment Distributors, Foodservice Manufacturers
Industry/Entity Type
Foodservice/Hospitality
Contact Information for Business Card
Name, Title, Contact Number, Email, Website, Social Media, Address
Requirements
Must have
- Clean & Simple but Serious and Impressionable

```html
<!DOCTYPE html>
<html lang="en">
<head>
<meta charset="utf-8">
<title>Meridian Service Partners – Business Card</title>
<link rel="stylesheet" href="https://fonts.googleapis.com/css2?family=Cinzel:wght@700&family=Tinos:wght@400;700&display=swap">
<style>
  :root {
    --navy: #2b2a7c;
    --white: #ffffff;
    --grey-swoosh: #bdbdbd;
    --ink: #111111;
    --backdrop: #1f1f22;
  }
  * { box-sizing: border-box; margin: 0; padding: 0; }
  html, body { width: 1200px; height: 900px; overflow: hidden; }
  body {
    background: var(--backdrop);
    display: flex;
    align-items: center;
    justify-content: center;
    gap: 40px;
  }
  .card {
    position: relative;
    width: 560px;
    height: 320px;
    border-radius: 22px;
    overflow: hidden;
  }

  /* Wordmark: plain name with one circle */
  .wordmark {
    display: flex;
    align-items: center;
    font-family: "Tinos", serif;
    font-weight: 700;
  }
  .wordmark__dot { border-radius: 50%; flex: none; }

  /* Front */
  .card--front {
    background: var(--navy);
    color: var(--white);
    display: flex;
    align-items: center;
    justify-content: center;
  }
  .card--front .wordmark { gap: 14px; font-size: 34px; }
  .card--front .wordmark__dot { width: 22px; height: 22px; background: var(--white); }

  /* Back */
  .card--back { background: var(--white); }
  .card__wave { position: absolute; inset: 0; width: 100%; height: 100%; }
  .card--back .wordmark {
    position: absolute;
    left: 34px;
    top: 110px;
    width: 250px;
    gap: 10px;
    font-size: 20px;
    line-height: 1.2;
    color: var(--navy);
  }
  .card--back .wordmark__dot { width: 14px; height: 14px; background: var(--navy); }

  .card__divider {
    position: absolute;
    left: 300px;
    top: 64px;
    width: 1.5px;
    height: 170px;
    background: var(--navy);
  }
  .contact {
    position: absolute;
    left: 318px;
    top: 62px;
    font-family: "Tinos", serif;
    color: var(--ink);
    font-size: 13px;
    line-height: 1.35;
  }
  .contact__name {
    font-family: "Cinzel", serif;
    font-weight: 700;
    color: var(--navy);
    font-size: 21px;
    line-height: 1.1;
  }
  .contact__title { margin-bottom: 4px; }
  .contact__row { display: flex; align-items: center; gap: 6px; }
  .contact__icon { width: 12px; height: 12px; flex: none; fill: var(--navy); }
  .contact__dot { width: 12px; height: 12px; border-radius: 50%; background: var(--navy); flex: none; }
</style>
</head>
<body>

  <section class="card card--front" aria-label="Card front">
    <div class="wordmark">
      <span class="wordmark__dot" aria-hidden="true"></span>
      <span class="wordmark__name">Meridian Service Partners</span>
    </div>
  </section>

  <section class="card card--back" aria-label="Card back">
    <svg class="card__wave" viewBox="0 0 560 320" preserveAspectRatio="none" aria-hidden="true">
      <path d="M0,92 C18,170 80,208 190,222 C120,206 44,176 0,110 Z" fill="var(--grey-swoosh)"/>
      <path d="M0,112 C34,182 96,214 190,224 C300,236 370,246 430,320 L0,320 Z" fill="var(--navy)"/>
    </svg>

    <div class="wordmark">
      <span class="wordmark__dot" aria-hidden="true"></span>
      <span class="wordmark__name">Meridian Service Partners</span>
    </div>

    <div class="card__divider"></div>

    <div class="contact">
      <div class="contact__name">DANIEL HARLOW</div>
      <div class="contact__title">Co-Founder</div>
      <div>P.O. BOX 41-06 NRT-52</div>
      <div>Linden Ave 14, Fairmont</div>
      <div class="contact__row">
        <svg class="contact__icon" viewBox="0 0 24 24" aria-hidden="true"><path d="M6.6 10.8a15 15 0 0 0 6.6 6.6l2.2-2.2a1 1 0 0 1 1-.25 11.4 11.4 0 0 0 3.6.6 1 1 0 0 1 1 1V20a1 1 0 0 1-1 1A17 17 0 0 1 3 4a1 1 0 0 1 1-1h3.5a1 1 0 0 1 1 1c0 1.25.2 2.45.6 3.6a1 1 0 0 1-.25 1z"/></svg>
        <span>555-014-2367</span>
      </div>
      <div class="contact__row">
        <svg class="contact__icon" viewBox="0 0 24 24" aria-hidden="true"><path d="M2 5h20v14H2z M2 5l10 8 10-8" fill="none" stroke="var(--navy)" stroke-width="2.2"/></svg>
        <span>info@meridianservice.com</span>
      </div>
      <div class="contact__row">
        <svg class="contact__icon" viewBox="0 0 24 24" aria-hidden="true"><circle cx="12" cy="12" r="9" fill="none" stroke="var(--navy)" stroke-width="2"/><path d="M3 12h18M12 3c3 3 3 15 0 18M12 3c-3 3-3 15 0 18" fill="none" stroke="var(--navy)" stroke-width="1.6"/></svg>
        <span>www.meridianservice.com</span>
      </div>
      <div class="contact__row">
        <span class="contact__dot"></span>
        <span>@meridianservice</span>
      </div>
    </div>
  </section>

</body>
</html>
```